Vemtra Group: Business Card for a high end technology company

We need a cool new design for our business cards using our cloud logo. We are a technology consulting business. We pride ourselves on be the best of the best. We mainly focus on cloud solutions and managed services. We need a business card that sets us apart from the other technology companies in the area and allows us to stand out.

Target Market(s)

Technology departments, CIO, CEOs, and Information Technology Staff.

Industry/Entity Type

Information Technology

Contact Information for Business Card

Must have the logo and our name.
Must have employee name, email address, office phone, cell phone and website.
Need to have all info on one side a cool design on backside.

Font styles to use
Serif
Sans Serif

Requirements
Must have
• Must have the logo and our name.
• Must have employee name, email address, office phone, cell phone and website.
• Need to have all info on one side a cool design on back side.
• Must be a crisp clean design, not too busy or confusing.

```html
<!DOCTYPE html>
<html lang="en">
<head>
<meta charset="utf-8">
<title>Vemtra Group – Business Card</title>
<link rel="stylesheet" href="https://fonts.googleapis.com/css2?family=Quicksand:wght@400&family=Open+Sans:wght@400;600;700&display=swap">
<style>
  :root {
    --backdrop: #3a3430;
    --card: #0c0c0d;
    --card-edge: #1a1a1c;
    --accent: #1ea0f0;
    --accent-deep: #0f6fd0;
    --silver: #d9d9d9;
    --text: #f2f2f2;
    --muted: #cfcfcf;
  }
  * { box-sizing: border-box; margin: 0; padding: 0; }
  html, body {
    width: 1200px; height: 900px; overflow: hidden;
    background: var(--backdrop);
  }
  .canvas {
    width: 1200px; height: 900px;
    display: flex; align-items: center; justify-content: center; gap: 40px;
  }
  .card {
    width: 520px; height: 297px;
    background: var(--card);
    border: 1px solid var(--card-edge);
    box-shadow: 0 14px 30px rgba(0,0,0,.45);
    position: relative;
  }
  /* Front */
  .card-front { display: flex; align-items: center; }
  .brand-block {
    width: 255px; padding-left: 34px;
    display: flex; flex-direction: column; align-items: flex-start; gap: 6px;
  }
  .brand-line { display: flex; align-items: center; gap: 10px; }
  .brand-dot {
    width: 16px; height: 16px; border-radius: 50%;
    background: var(--accent);
  }
  .brand-name {
    font-family: "Quicksand", sans-serif; font-weight: 400;
    font-size: 30px; color: var(--silver); letter-spacing: .5px;
  }
  .brand-web {
    font-family: "Open Sans", sans-serif; font-weight: 700;
    font-size: 11px; color: var(--text); letter-spacing: .6px;
    padding-left: 26px;
  }
  .divider {
    width: 1px; height: 150px;
    background: linear-gradient(var(--accent-deep), var(--accent));
  }
  .details { padding-left: 26px; font-family: "Open Sans", sans-serif; }
  .person-name { font-weight: 700; font-size: 15px; color: var(--accent); }
  .person-role { font-size: 11px; color: var(--text); margin-bottom: 22px; }
  .contact-list { list-style: none; display: flex; flex-direction: column; gap: 5px; }
  .contact-item {
    display: flex; align-items: center; gap: 9px;
    font-size: 12px; color: var(--text);
  }
  .contact-icon { width: 10px; height: 10px; fill: var(--accent); flex: none; }
  /* Back */
  .card-back {
    display: flex; flex-direction: column; align-items: center; justify-content: center; gap: 8px;
  }
  .back-name {
    font-family: "Quicksand", sans-serif; font-weight: 400;
    font-size: 46px; color: var(--silver); letter-spacing: 1px;
  }
  .back-web {
    font-family: "Open Sans", sans-serif; font-weight: 700;
    font-size: 14px; color: var(--silver); letter-spacing: 1px;
  }
</style>
</head>
<body>
<main class="canvas">
  <section class="card card-front" aria-label="Business card front">
    <div class="brand-block">
      <div class="brand-line">
        <span class="brand-dot"></span>
        <span class="brand-name">Vemtra Group</span>
      </div>
      <span class="brand-web">www.vemtragroup.com</span>
    </div>
    <div class="divider"></div>
    <div class="details">
      <p class="person-name">Daniel Okafor</p>
      <p class="person-role">Managing Director</p>
      <ul class="contact-list">
        <li class="contact-item">
          <svg class="contact-icon" viewBox="0 0 10 10" aria-hidden="true"><path d="M2 0.5 L3.6 2.8 L2.8 3.8 Q4 6.2 6.2 7.2 L7.2 6.4 L9.5 8 L8.3 9.5 Q3.5 9 0.5 1.7 Z"/></svg>
          044-555 018 274
        </li>
        <li class="contact-item">
          <svg class="contact-icon" viewBox="0 0 10 10" aria-hidden="true"><path d="M0 2 H10 V8.5 H0 Z M0.8 2.6 L5 5.6 L9.2 2.6" stroke="#0c0c0d" stroke-width=".8"/></svg>
          info@vemtramail.com
        </li>
        <li class="contact-item">
          <svg class="contact-icon" viewBox="0 0 10 10" aria-hidden="true"><circle cx="5" cy="5" r="5"/></svg>
          www.vemtrasite.com
        </li>
      </ul>
    </div>
  </section>

  <section class="card card-back" aria-label="Business card back">
    <span class="back-name">Vemtra Group</span>
    <span class="back-web">www.vemtragroup.com</span>
  </section>
</main>
</body>
</html>
```